Coaching Services Flyer

I need a two page flyer to promote by coaching (life and business coaching services) something like this: http://quillmarshden.net/downloads/Dana-Petrov-Workshops-and-Coaching-2015.pdf

My primary client is small business owners who are looking for help reaching their business goals.

Please incorporate my logo below and if possible, the compass symbol. I want something that speaks to finding your direction. The colors are bold so the design needs to soften the overall look a bit since it's a coaching service.

Also incorporate the quote from Theodoric: “Excellence is never an accident. It is always the result of high intention, sincere effort, and intelligent execution; it represents the wise choice of many alternatives - choice, not chance, determines your destiny.”

```html
<!DOCTYPE html>
<html lang="en">
<head>
<meta charset="utf-8">
<title>Halvard – Life and Business Coaching Services Flyer</title>
<link rel="stylesheet" href="https://fonts.googleapis.com/css2?family=Open+Sans:ital,wght@0,300;0,400;0,600;1,400&display=swap">
<style>
  :root {
    --navy: #2a2a7c;
    --red: #d3202a;
    --ink: #111111;
    --body: #555555;
    --paper: #ffffff;
    --sky-top: #8a9aa6;
    --sky-bottom: #d9e0e4;
    --sky-blue: #4f8fd6;
    --sky-pale: #cfe2f4;
  }
  * { box-sizing: border-box; margin: 0; padding: 0; }
  html, body { width: 1200px; height: 847px; overflow: hidden; background: var(--paper); }
  body { font-family: "Open Sans", Arial, sans-serif; color: var(--body); }
  .flyer { position: relative; width: 1200px; height: 847px; display: flex; }
  .page { position: relative; width: 600px; height: 847px; overflow: hidden; background: var(--paper); }
  .page + .page { border-left: 1px solid #e6e6e6; }
  .shapes { position: absolute; inset: 0; width: 600px; height: 847px; }

  .brand {
    position: absolute; left: 35px; top: 10px;
    font-size: 50px; font-weight: 400; color: var(--ink); letter-spacing: 1px; line-height: 1;
  }
  .contact { position: absolute; left: 283px; top: 10px; color: #333; font-size: 11px; line-height: 14px; white-space: nowrap; }
  .contact h1 { font-size: 18px; font-weight: 400; color: var(--ink); line-height: 24px; margin-bottom: 1px; white-space: nowrap; }
  .contact b { font-weight: 600; }

  .hero-title {
    position: absolute; left: 37px; top: 214px;
    color: var(--paper); font-weight: 300; font-size: 37px; line-height: 42px; letter-spacing: 1px;
  }

  .badge {
    position: absolute; width: 96px; height: 96px; border-radius: 50%;
    background: var(--paper); border: 5px solid var(--navy);
    display: flex; align-items: center; justify-content: center; text-align: center;
    padding: 14px 0 0 12px;
    color: var(--ink); font-size: 13px; font-weight: 600; line-height: 16px;
  }
  .badge::before {
    content: ""; position: absolute; left: -26px; top: -4px;
    width: 34px; height: 34px; border-radius: 50%;
    background: var(--navy); border: 3px solid var(--paper); box-shadow: 0 0 0 2px var(--navy);
  }

  .column {
    position: absolute; width: 170px;
    font-size: 10px; line-height: 12.2px; letter-spacing: -0.1px; text-align: justify; color: var(--body);
  }
  .wide {
    position: absolute; width: 556px;
    font-size: 10.2px; line-height: 12.2px; text-align: justify; color: var(--body);
  }
  .quote {
    position: absolute; left: 22px; top: 622px; width: 570px;
    font-style: italic; font-size: 14px; line-height: 18px; color: #222;
  }
  .tagline {
    position: absolute; left: 26px; top: 614px;
    font-size: 35px; font-weight: 400; color: var(--ink); letter-spacing: 1px;
    transform: rotate(-11.5deg); transform-origin: left bottom; white-space: nowrap;
  }
</style>
</head>
<body>
<main class="flyer">

  <section class="page page-front">
    <svg class="shapes" viewBox="0 0 600 847" aria-hidden="true">
      <defs>
        <linearGradient id="skyGrey" x1="0" y1="0" x2="0" y2="1">
          <stop offset="0" stop-color="var(--sky-top)"/>
          <stop offset="1" stop-color="var(--sky-bottom)"/>
        </linearGradient>
      </defs>
      <polygon points="0,128 600,64 600,96 0,140" fill="var(--red)"/>
      <polygon points="0,300 600,290 600,345 0,420" fill="var(--navy)"/>
      <polygon points="600,775 600,847 240,847" fill="var(--red)"/>
    </svg>
    <svg class="shapes" viewBox="0 0 600 847" role="img" aria-label="Photo of a businesswoman holding a colourful umbrella on a diving board against a grey sky">
      <polygon points="0,140 600,96 600,290 0,405" fill="url(#skyGrey)"/>
    </svg>

    <div class="brand">Halvard</div>
    <div class="contact">
      <h1>Life and Business Coaching Services</h1>
      RR#3, Fenwick Hollow, Nova Scotia, Canada B0X 2K4<br>
      <b>phone:</b> 902.555.0148<br>
      <b>e-mail:</b> dana@quillmarshden.net
    </div>

    <h2 class="hero-title">FINDING YOUR<br>DIRECTION</h2>

    <div class="badge" style="left:52px; top:348px;">ABOUT<br>ME</div>
    <div class="badge" style="left:246px; top:304px;">SERVICES<br>OFFERED</div>
    <div class="badge" style="left:450px; top:261px;">TRAINING<br>PROGRAM</div>

    <p class="column" style="left:17px; top:461px;">Lorem Ipsum is simply dummy text of the printing and typesetting industry. Lorem Ipsum has been the industry's standard dummy text ever since the 1500s, when an unknown printer took a galley of type and scrambled it to make a type specimen book. It has survived not only five centuries, but also the leap into electronic typesetting,</p>
    <p class="column" style="left:218px; top:426px;">Lorem Ipsum is simply dummy text of the printing and typesetting industry. Lorem Ipsum has been the industry's standard dummy text ever since the 1500s, when an unknown printer took a galley of type and scrambled it to make a type specimen book. It has survived not only five centuries, but also the leap into electronic typesetting, remaining essentially unchanged. It was popularisefive centurssentially unchanged. It was popularised in</p>
    <p class="column" style="left:416px; top:391px;">Lorem Ipsum is simply dummy text of the printing and typesetting industry. Lorem Ipsum has been the industry's standard dummy text ever since the 1500s, when an unknown printer took a galley of type and scrambled it to make a type specimen book. It has survived not only five centuries, but also the leap into electronic typesetting, remaining essentially unchanged. It was popularisefive centurssentially unchanged. It was popularised in the 1960s with the release of Letraset sheets containing Lorem Ipsum passages, and more recently</p>

    <blockquote class="quote">“Excellence is never an accident. It is always the result of high intention, sincere effort, and intelligent execution; it represents the wise choice of many alternatives - choice, not chance, determines your destiny.”- Theodoric</blockquote>

    <p class="wide" style="left:20px; top:697px;">Lorem Ipsum is simply dummy text of the printing and typesetting industry. Lorem Ipsum has been the industry's standard dummy text ever since the 1500s, when an unknown printer took a galley of type and scrambled it to make a type specimen book. It has survived not only five centuries, but also the leap into electronic typesetting, remaining essentially unchanged. It was popularisefive centurssentially unchanged. It was popularised in the 1960s with the release of Letraset sheets containing Lorem Ipsum passages, and more recently with desktop publishing software like Aldus PageMaker including versions of Lorem Ipsum.</p>
  </section>

  <section class="page page-back">
    <svg class="shapes" viewBox="0 0 600 847" aria-hidden="true">
      <polygon points="0,128 600,62 600,100 0,178" fill="var(--red)"/>
      <polygon points="0,682 600,558 600,612 0,700" fill="var(--navy)"/>
    </svg>
    <svg class="shapes" viewBox="0 0 600 847" role="img" aria-label="Photo of four cheering business people jumping against a blue sky">
      <defs>
        <linearGradient id="skyBlue" x1="0" y1="0" x2="0" y2="1">
          <stop offset="0" stop-color="var(--sky-blue)"/>
          <stop offset="1" stop-color="var(--sky-pale)"/>
        </linearGradient>
      </defs>
      <polygon points="0,700 600,612 600,847 0,847" fill="url(#skyBlue)"/>
    </svg>

    <div class="brand">Halvard</div>
    <div class="contact">
      <h1>Life and Business Coaching Services</h1>
      RR#3, Fenwick Hollow, Nova Scotia, Canada B0X 2K4<br>
      <b>phone:</b> 902.555.0148<br>
      <b>e-mail:</b> dana@quillmarshden.net
    </div>

    <div class="badge" style="left:44px; top:142px;">CENTRES<br>AVAILABLE</div>
    <div class="badge" style="left:238px; top:108px;">SPECIAL<br>OFFERS</div>
    <div class="badge" style="left:452px; top:80px;">ENROLL<br>NOW</div>

    <p class="column" style="left:15px; top:241px;">Lorem Ipsum is simply dummy text of the printing and typesetting industry. Lorem Ipsum has been the industry's standard dummy text ever since the 1500s, when an unknown printer took a galley of type and scrambled it to make a type specimen book. It has survived not only five centuries, but also the leap into electronic typesetting,</p>
    <p class="column" style="left:215px; top:207px;">Lorem Ipsum is simply dummy text of the printing and typesetting industry. Lorem Ipsum has been the industry's standard dummy text ever since the 1500s, when an unknown printer took a galley of type and scrambled it to make a type specimen book. It has survived not only five centuries, but also the leap into electronic typesetting, remaining essentially unchanged. It was popularisefive centurssentially unchanged. It was popularised in</p>
    <p class="column" style="left:414px; top:171px;">Lorem Ipsum is simply dummy text of the printing and typesetting industry. Lorem Ipsum has been the industry's standard dummy text ever since the 1500s, when an unknown printer took a galley of type and scrambled it to make a type specimen book. It has survived not only five centuries, but also the leap into electronic typesetting, remaining essentially unchanged. It was popularisefive centurssentially unchanged. It was popularised in the 1960s with the release of Letraset sheets containing Lorem Ipsum passages, and more recently</p>

    <p class="wide" style="left:22px; top:387px;">Lorem Ipsum is simply dummy text of the printing and typesetting industry. Lorem Ipsum has been the industry's standard dummy text ever since the 1500s, when an unknown printer took a galley of type and scrambled it to make a type specimen book. It has survived not only five centuries, but also the leap into electronic typesetting, remaining essentially unchanged. It was popularisefive centurssentially unchanged. It was popularised in the 1960s with the release of Letraset sheets containing Lorem Ipsum passages, and more recently with desktop publishing software like Aldus PageMaker including versions of Lorem Ipsum.</p>
    <p class="wide" style="left:22px; top:472px;">Lorem Ipsum is simply dummy text of the printing and typesetting industry. Lorem Ipsum has been the industry's standard dummy text ever since the 1500s, when an unknown printer took a galley of type and scrambled it to make a type specimen book. It has survived not only five centuries, but also the leap into electronic typesetting, remaining essentially unchanged. It was popularisefive centurssentially unchanged. It was popularised in the 1960s with the release of Letraset sheets containing Lorem Ipsum passages, and more recently with desktop publishing software like Aldus PageMaker including versions of Lorem Ipsum.</p>

    <h2 class="tagline">FINDING YOUR DIRECTION</h2>
  </section>

</main>
</body>
</html>
```